Tralvo GmbH banner ad

Banner ad for Facebook Our company name (logo) Title: Transporter and bus rental Text: Without deposit, super prices

Target Market(s)

Rental

Requirements
Must have
• LOGO from us, Evt. A pair of transporters in the picture

```html
<!DOCTYPE html>
<html lang="de">
<head>
<meta charset="UTF-8">
<title>Tralvo GmbH – Transporter und Bus Vermietung</title>
<link rel="stylesheet" href="https://fonts.googleapis.com/css2?family=Josefin+Sans:wght@300;400;700&display=swap">
<style>
  :root {
    --navy: #1c1a6e;
    --navy-deep: #16145e;
    --white: #ffffff;
    --sky-grey: #9aa3ad;
    --road-grey: #6f757c;
    --pale: #dfe3e7;
  }
  * { margin: 0; padding: 0; box-sizing: border-box; }
  html, body {
    width: 1200px;
    height: 444px;
    overflow: hidden;
    background: var(--white);
  }
  .banner {
    position: relative;
    width: 1200px;
    height: 444px;
    overflow: hidden;
    background: var(--white);
    font-family: "Josefin Sans", Arial, sans-serif;
  }
  .hero-photo {
    position: absolute;
    left: 0;
    top: 0;
    width: 820px;
    height: 444px;
    background:
      linear-gradient(to right, rgba(255,255,255,0) 0%, rgba(255,255,255,0) 55%, rgba(255,255,255,0.85) 80%, var(--white) 100%),
      linear-gradient(to bottom, var(--sky-grey) 0%, var(--pale) 45%, var(--road-grey) 100%);
  }
  .brand {
    position: absolute;
    left: 742px;
    top: 40px;
    display: flex;
    align-items: center;
    gap: 16px;
  }
  .brand-mark {
    width: 58px;
    height: 58px;
    background: var(--navy);
  }
  .brand-name {
    font-weight: 700;
    font-size: 46px;
    color: var(--navy);
    line-height: 1;
    padding-top: 6px;
  }
  .headline {
    position: absolute;
    left: 640px;
    width: 560px;
    top: 188px;
    text-align: center;
    color: var(--navy);
    font-weight: 700;
    font-size: 58px;
    line-height: 64px;
  }
  .offer {
    position: absolute;
    left: 600px;
    top: 330px;
    width: 640px;
    height: 82px;
  }
  .offer svg {
    position: absolute;
    inset: 0;
  }
  .offer-text {
    position: absolute;
    left: 40px;
    right: 40px;
    top: 0;
    height: 82px;
    display: flex;
    align-items: center;
    justify-content: center;
    color: var(--white);
    font-weight: 300;
    font-size: 38px;
    padding-top: 6px;
  }
</style>
</head>
<body>
  <div class="banner">
    <div class="hero-photo" role="img" aria-label="Weißer Sattelzug mit Kühlauflieger in voller Fahrt auf der Straße, mit Bewegungsunschärfe"></div>

    <div class="brand">
      <div class="brand-mark"></div>
      <span class="brand-name">Tralvo GmbH</span>
    </div>

    <h1 class="headline">Transporter und<br>Bus Vermietung</h1>

    <div class="offer">
      <svg width="640" height="82" viewBox="0 0 640 82" aria-hidden="true">
        <polygon points="24,4 640,4 640,78 4,78" fill="var(--navy-deep)" stroke="var(--white)" stroke-width="4"/>
      </svg>
      <p class="offer-text">Ohne Kaution, Superpreise</p>
    </div>
  </div>
</body>
</html>
```